Willowmere Counseling (Endure - Mend - Flourish) - Double Sided Business Card

I would like a 2-sided business card. Front: Matte Black or Navy with Logo & Tagline. Back: Name, Address, Phone Number, Email, & Website (maybe would like to include a small map pin-pointing location); Prefer front to be a gold/silver foil (iridescent); Back prefer white or light colored background with lettering that is easy to read and simple

Target Market(s)

Individuals & Couples (13 y.o. - ALL Adults); High end clientele

Industry/Entity Type

Licensed Professional Counselor (Mental Health)

Contact Information for Business Card

Name: Willowmere Counseling; Tagline: Endure - Mend - Flourish; Address: 3870 N. Garrick Ave., Suite 214, Fort Worth, TX 76132; Phone: (214) 555-0187; Website: www.WillowmereCounseling.example

Font styles to use
Serif

Requirements
Must have
• Logo on Front (Large) prefer gold/silver foil on a matte dark color (i.e. black, navy, etc.); Back of Card: All other relevant information

```html
<!DOCTYPE html>
<html lang="en">
<head>
<meta charset="utf-8">
<title>Willowmere Counseling – Business Card</title>
<link rel="stylesheet" href="https://fonts.googleapis.com/css2?family=Cinzel:wght@400;500&family=Arimo:wght@400&display=swap">
<style>
  :root {
    --backdrop: #343434;
    --card-white: #ffffff;
    --card-grey: #6b6c6e;
    --panel-grey: #818386;
    --gold: #d4b65a;
    --text-grey: #4a4a4a;
  }
  html, body {
    margin: 0;
    padding: 0;
    width: 1200px;
    height: 1200px;
    overflow: hidden;
    background: var(--backdrop);
  }
  .canvas {
    position: relative;
    width: 1200px;
    height: 1200px;
  }
  .card {
    position: absolute;
    left: 262px;
    width: 686px;
    height: 392px;
    border-radius: 20px;
    overflow: hidden;
  }
  .card--contact { top: 165px; background: var(--card-white); }
  .card--brand {
    top: 653px;
    background: var(--card-grey);
    display: flex;
    flex-direction: column;
    align-items: center;
    justify-content: center;
  }

  /* Contact side */
  .brand-block {
    position: absolute;
    left: 37px;
    top: 52px;
    width: 270px;
  }
  .brand-name {
    margin: 0;
    font-family: "Cinzel", serif;
    font-weight: 500;
    font-size: 30px;
    line-height: 1.05;
    color: var(--gold);
    letter-spacing: 0.5px;
  }
  .brand-tagline {
    margin: 8px 0 0;
    font-family: "Cinzel", serif;
    font-size: 12px;
    color: var(--gold);
    letter-spacing: 0.3px;
  }
  .accent-bar {
    position: absolute;
    left: 0;
    top: 160px;
    width: 8px;
    height: 38px;
    background: var(--gold);
  }
  .person {
    position: absolute;
    left: 37px;
    top: 160px;
  }
  .person-name {
    margin: 0;
    font-family: "Cinzel", serif;
    font-weight: 500;
    font-size: 23px;
    line-height: 1;
    color: var(--gold);
  }
  .person-title {
    margin: 4px 0 0;
    font-family: "Arimo", sans-serif;
    font-size: 14px;
    color: var(--text-grey);
  }
  .address {
    position: absolute;
    left: 37px;
    top: 222px;
    margin: 0;
    font-family: "Arimo", sans-serif;
    font-style: normal;
    font-size: 14px;
    line-height: 19.5px;
    color: var(--text-grey);
  }
  .contact-list {
    position: absolute;
    left: 37px;
    top: 294px;
    margin: 0;
    padding: 0;
    list-style: none;
    font-family: "Arimo", sans-serif;
    font-size: 14px;
    line-height: 19.5px;
    color: var(--text-grey);
    white-space: nowrap;
  }
  .contact-list li {
    display: flex;
    align-items: center;
    gap: 9px;
  }
  .contact-icon { width: 12px; height: 12px; flex: none; }
  .artwork-panel {
    position: absolute;
    left: 345px;
    top: 0;
    width: 341px;
    height: 392px;
    background: linear-gradient(115deg, var(--card-white) 0%, var(--gold) 30%, var(--card-white) 60%, var(--panel-grey) 100%);
  }

  /* Brand side */
  .brand-mark {
    width: 22px;
    height: 22px;
    border-radius: 50%;
    background: var(--gold);
    margin-bottom: 18px;
  }
  .brand-side-name {
    margin: 0;
    font-family: "Cinzel", serif;
    font-weight: 500;
    font-size: 38px;
    color: var(--gold);
    letter-spacing: 0.5px;
  }
  .brand-side-tagline {
    margin: 8px 0 0;
    font-family: "Cinzel", serif;
    font-size: 14px;
    color: var(--gold);
    letter-spacing: 0.4px;
  }
</style>
</head>
<body>
<main class="canvas">
  <section class="card card--contact">
    <div class="artwork-panel" role="img" aria-label="Large gold and grey brand artwork area"></div>

    <div class="brand-block">
      <h1 class="brand-name">Willowmere<br>Counseling</h1>
      <p class="brand-tagline">Endure - Mend - Flourish</p>
    </div>

    <div class="accent-bar"></div>
    <div class="person">
      <h2 class="person-name">Daniel Harper</h2>
      <p class="person-title">President</p>
    </div>

    <address class="address">
      3870 N. Garrick Ave.<br>
      Suite 214<br>
      Fort Worth, TX 76132
    </address>

    <ul class="contact-list">
      <li>
        <svg class="contact-icon" viewBox="0 0 16 16" aria-hidden="true"><path fill="#d4b65a" d="M3.6 1.2l2.3 2.6c.3.4.3.9 0 1.2L4.8 6.2c.8 1.8 2.2 3.3 4 4.1l1.2-1.1c.3-.3.9-.3 1.2 0l2.6 2.3c.4.3.4.9 0 1.3l-1.3 1.3c-.6.6-1.6.8-2.4.4C6.4 13 3 9.6 1.4 5.9 1 5.1 1.2 4.1 1.8 3.5L3 2.2c.2-.4.3-1 .6-1z"/></svg>
        (214) 555-0187
      </li>
      <li>
        <svg class="contact-icon" viewBox="0 0 16 16" aria-hidden="true"><rect x="1" y="3.5" width="14" height="9.5" fill="#d4b65a"/><path d="M1.5 4l6.5 5 6.5-5" fill="none" stroke="#fff" stroke-width="1.2"/></svg>
        info@WillowmereCounseling.example
      </li>
      <li>
        <svg class="contact-icon" viewBox="0 0 16 16" aria-hidden="true"><circle cx="8" cy="8" r="6.8" fill="#d4b65a"/><path d="M1.5 8h13M8 1.2c-2.4 2.2-2.4 11.4 0 13.6M8 1.2c2.4 2.2 2.4 11.4 0 13.6" fill="none" stroke="#fff" stroke-width="1"/></svg>
        www.WillowmereCounseling.example
      </li>
    </ul>
  </section>

  <section class="card card--brand">
    <div class="brand-mark"></div>
    <h2 class="brand-side-name">Willowmere Counseling</h2>
    <p class="brand-side-tagline">Endure - Mend - Flourish</p>
  </section>
</main>
</body>
</html>
```